Flyer Needed to Advertise New Online Reading Programs

ABOUT THE ACADEMY OF LITERACY GROWTH
The Institute teaches summer reading skills programs for elementary school students, in programs offered through partnerships with universities, colleges and municipalities nationwide. The goal of each program is to build reading skills, and to foster a lifetime love of books and reading.

AIMS & TARGET MARKET
The Institute has developed a new format of its’ online reading program for elementary students, which includes live small-group video classes taught by a professional reading teacher. The Institute seeks a new graphic design for a flyer to advertise the new online reading program. The flyer will be sent to elementary schools, passed out by teachers, and then taken home by students to show parents; therefore, the primary audience for the flyer will be teachers and parents of elementary school students.

Live classes for children are completely new in online education, unlike anything else in the marketplace, and parents and teachers therefore have no experience with them. The successful design will include illustrations or photographs that allow visitors to immediately grasp/understand the new video class format, without relying heavily on a written description. Additionally, the successful flyer concept will make the program, and the video classes in particular, feel fun and appealing to kids and parents.

Below is additional information about the new live small-group video class format, which meets weekly for 6 weeks:
o During video classes, students participate from home.
o During discussions, the student’s computer (or tablet) screen is filled with live video frames of the teacher and the other students. The video frame for the teacher is larger, and the other students appear in smaller frames.
o During other video class instruction, the teacher uses a presentation screen to display pages of a book or a “whiteboard” used for instructional activities.

Notes: The flyer design could include an illustrated or photo screenshot of a video class, with children looking engaged and a teacher leading them in discussion (stock photos are okay to use in flyer design). We have included a screen shot of one of these classes for reference, but do not feel constrained to represent this screen realistically (as shown here). Layout, look and feel can be changed. Alternatively, you may choose to use a graphic other than a screenshot to bring across the concept of the video classes.

COPY AND SPECIFICATIONS
The flyer design will be one-sided and the dimensions are 8.5” x 11” in either portrait or landscape orientation. We will consider designs in color or black and white. Since we brand our flyers with logos of the universities we partner with throughout the nation, we’ll need to include a partner logo in the design. Exact copy will be provided, but layout is flexible. Screenshots from our sample classes are included to show screen layout. Stock photos are okay to use in flyer designs.

Hi designers, We wanted to share our thoughts on the main image of the flyer. We're leaning towards an image that shows a sole student on a computer with the computer screen in view. The computer screen could have the sample image we provided to show how the video classes operate. Thanks! The Academy of Literacy Growth

```html
<!DOCTYPE html>
<html lang="en">
<head>
<meta charset="utf-8">
<title>Reading Skills Classes – Online this Summer</title>
<link rel="stylesheet" href="https://fonts.googleapis.com/css2?family=Lato:wght@300;400;700;900&family=Open+Sans:ital,wght@0,400;0,700;1,700&display=swap">
<style>
  :root {
    --page-bg: #5f8088;
    --cyan: #16b6d6;
    --panel-dark: #252525;
    --paper: #ffffff;
    --ink: #1c1c1c;
    --body-ink: #3a3a3a;
    --muted-line: #5a5a5a;
    --photo-a: #c9c1ad;
    --photo-b: #8a8a7c;
  }
  * { margin: 0; padding: 0; box-sizing: border-box; }
  html, body { width: 800px; height: 1200px; overflow: hidden; }
  body {
    background: var(--page-bg);
    font-family: "Open Sans", sans-serif;
    position: relative;
  }
  .flyer {
    position: absolute;
    left: 77px; top: 197px;
    width: 647px; height: 836px;
    background: var(--paper);
    box-shadow: 0 10px 30px rgba(0,0,0,.25);
  }
  .title-panel {
    position: absolute; left: 0; top: 0;
    width: 231px; height: 278px;
    background: var(--cyan);
    color: #fff;
    font-family: "Lato", sans-serif;
    padding: 36px 0 0 16px;
  }
  .title-panel h1 {
    font-weight: 700;
    font-size: 49px;
    line-height: 56px;
    letter-spacing: .5px;
  }
  .title-panel h1 .small { font-size: 39px; display: block; line-height: 50px; }
  .title-panel .tagline {
    font-weight: 400;
    font-size: 21px;
    margin-top: 4px;
    white-space: nowrap;
  }
  .hero-photo {
    position: absolute; left: 231px; top: 0;
    width: 416px; height: 278px;
    background: linear-gradient(120deg, var(--photo-a) 0%, #d8d2c2 45%, var(--photo-b) 100%);
  }
  .side-panel {
    position: absolute; left: 0; top: 278px;
    width: 231px; height: 558px;
    background: var(--panel-dark);
    color: #fff;
  }
  .features { list-style: none; position: absolute; left: 13px; top: 0; }
  .features li {
    position: absolute; left: 0;
    display: flex; align-items: center; gap: 7px;
    width: 215px;
    font-size: 11.5px; line-height: 15px;
  }
  .features svg { flex: none; width: 26px; height: 26px; }
  .divider {
    position: absolute; left: 10px; width: 211px;
    border-top: 1px solid var(--muted-line);
  }
  .skills { list-style: none; position: absolute; left: 26px; top: 228px; }
  .skills li {
    position: relative;
    padding-left: 22px;
    font-family: "Lato", sans-serif;
    font-weight: 700;
    font-size: 12px;
    line-height: 22.2px;
  }
  .skills li::before {
    content: ""; position: absolute; left: 0; top: 8px;
    width: 7px; height: 7px; border-radius: 50%;
    background: var(--cyan);
  }
  .partner-name {
    position: absolute; left: 28px; top: 470px;
    width: 175px;
    font-family: "Lato", sans-serif;
    font-weight: 400;
    font-size: 20px; line-height: 24px;
    letter-spacing: 1px;
    text-align: center;
    color: #fff;
  }
  .programs { position: absolute; left: 251px; top: 294px; width: 392px; }
  .program { position: absolute; left: 0; width: 392px; }
  .program h2 {
    font-size: 11.5px; font-weight: 700; color: var(--ink);
    line-height: 14px;
  }
  .program p {
    font-size: 9.3px; line-height: 12.6px; color: var(--body-ink);
  }
  .contact {
    position: absolute; right: 10px; top: 750px;
    text-align: right; color: var(--ink);
  }
  .contact h3 { font-size: 16px; font-weight: 700; line-height: 22px; }
  .contact .phone { font-size: 16.5px; font-weight: 700; font-style: italic; line-height: 22px; }
  .contact .hours { font-size: 11px; margin-top: 8px; word-spacing: 1px; }
  .contact .hours b { margin-left: 12px; }
  .contact .hours b:first-child { margin-left: 0; }
</style>
</head>
<body>
<main class="flyer">
  <header class="title-panel">
    <h1>Reading Skills <span class="small">Classes</span></h1>
    <p class="tagline">Online this Summer!</p>
  </header>

  <div class="hero-photo" role="img" aria-label="Photo of a young student with headphones at a laptop, joining a live video reading class"></div>

  <aside class="side-panel">
    <ul class="features">
      <li style="top:35px">
        <svg viewBox="0 0 26 26"><circle cx="13" cy="13" r="12.5" fill="#16b6d6"/><rect x="7" y="8" width="12" height="8.5" rx="1" fill="none" stroke="#fff" stroke-width="1.4"/><rect x="5.5" y="17.5" width="15" height="1.6" fill="#fff"/></svg>
        Small class size
      </li>
      <li style="top:73px">
        <svg viewBox="0 0 26 26"><circle cx="13" cy="13" r="12.5" fill="#16b6d6"/><circle cx="13" cy="8" r="2.6" fill="#fff"/><path d="M9 16 Q9 11 13 11 Q17 11 17 16Z" fill="#fff"/><rect x="8.5" y="15" width="9" height="5" fill="#fff"/></svg>
        A skilled and encouraging teacher
      </li>
      <li style="top:112px">
        <svg viewBox="0 0 26 26"><circle cx="13" cy="13" r="12.5" fill="#16b6d6"/><circle cx="13" cy="9.5" r="3.2" fill="#fff"/><path d="M7 19 Q7 13.5 13 13.5 Q19 13.5 19 19Z" fill="#fff"/></svg>
        Individualized skills intruction
      </li>
      <li style="top:151px">
        <svg viewBox="0 0 26 26"><circle cx="13" cy="13" r="12.5" fill="#16b6d6"/><rect x="8.5" y="7" width="9" height="12" rx="1" fill="#fff"/><rect x="10" y="9" width="6" height="1.2" fill="#16b6d6"/></svg>
        A program of independent<br>reading in great books
      </li>
    </ul>
    <div class="divider" style="top:207px"></div>
    <ul class="skills">
      <li>Phonics</li>
      <li>Comprehension</li>
      <li>Fluency</li>
      <li>Study Skills</li>
      <li>Speed Reading</li>
      <li>Love of Reading</li>
    </ul>
    <div class="divider" style="top:385px"></div>
    <p class="partner-name">HARBORVIEW<br>UNIVERSITY</p>
  </aside>

  <section class="programs">
    <article class="program" style="top:0">
      <h2>Program for Preschoolers:</h2>
      <p>Students in this program build strong reading readiness skills.<br>Your child will learn letter recognition and beginning phonics, and develop the motivation and love of reading that make learning to read easy, enjoyable, and successful.</p>
    </article>
    <article class="program" style="top:61px">
      <h2>Program for Entering Kindergartners:</h2>
      <p>Students in this program learn beginning reading skills and develop a love of books. Your child will learn letter recognition, phonics, and sight words, and will learn to sound out short words.</p>
    </article>
    <article class="program" style="top:122px">
      <h2>Program for Entering 1st Graders:</h2>
      <p>Students in this program learn to read independently. Your child will learn phonics and sight words, build comprehension, and gain the skills and confidence needed for success in first grade.</p>
    </article>
    <article class="program" style="top:182px">
      <h2>Program for Entering 2nd Graders:</h2>
      <p>Students in this program become fluent, independent readers. Your child will make significant gains in phonics and word-attack skills, fluency, and comprehension, and will develop confidence and a love of reading.</p>
    </article>
    <article class="program" style="top:246px">
      <h2>Program for Entering 3rd Graders:</h2>
      <p>Students in this program become strong independent readers. Your child will develop the comprehension, fluency, and long-word decoding skills needed to read longer books with ease, and will build confidence and a love of reading.</p>
    </article>
    <article class="program" style="top:308px">
      <h2>Program for Entering 4th and 5th Graders:</h2>
      <p>Students in this program make substantial gains in comprehension, long-word decoding skills, fluency, and reading speed. Your child will complete homework more quickly and easily, be more successful in school, and become a strong, enthusiastic reader.</p>
    </article>
    <article class="program" style="top:380px">
      <h2>Programs for Entering 6th-8th Graders and Entering 9th and 10th Graders:</h2>
      <p>Students in these programs make substantial gains in comprehension while doubling reading speed. They also learn the best way to read textbooks, take notes, and study for tests. As a result, students complete homework more quickly and easily, get better grades, and enjoy reading more.</p>
    </article>
  </section>

  <footer class="contact">
    <h3>For More Information or to Register</h3>
    <p class="phone">Call 1-800-555-0142</p>
    <p class="hours"><b>Mon.-Fri :</b> 5am - 7pm <b>Sat :</b> 5am - 4pm <b>Sun :</b> 6am- 4pm</p>
  </footer>
</main>
</body>
</html>
```